Ancient Art and Artifact information website

Hello Designers,
We are starting up a new website who talk abut and discusses an ancient arts artifacts. We would covering a wide range of countries ranging from Egypt, Greece, India, Syria, Rome, etc. My website name Tarn Wisp
Designs that fits with ancient theme and some kind of uniqueness would be accepted.
Requirements:
1) A home page design
2) Sub page design
3) A suitable logo
Sections can be added are featured ancient arts/places with short description followed by a more button, latest news, and comment section.
Add contents if you found relevant for this category of website. Ability to share the information through social media is desired.
Must be a responsive design. I look forward to designs which are mind blowing.
Number of Pages Required
2 page

```html
<!DOCTYPE html>
<html lang="en">
<head>
<meta charset="utf-8">
<title>Tarn Wisp – Ancient Arts and Artifacts</title>
<link href="https://fonts.googleapis.com/css2?family=Open+Sans:ital,wght@0,400;0,600;0,700;0,800;1,600&display=swap" rel="stylesheet">
<style>
:root{
  --ink:#2a1a0c;
  --white:#ffffff;
  --brown:#a4682e;
  --brown-dark:#8e5624;
  --card:#9c6230;
  --amber:#b9822f;
  --parchment:#e3aa5c;
  --parchment-light:#eec07a;
  --orange:#f7941d;
  --yellow:#ffe21a;
  --nav:#ffffff;
}
*{margin:0;padding:0;box-sizing:border-box}
html,body{width:1200px;height:2848px;overflow:hidden}
body{position:relative;font-family:"Open Sans",Arial,sans-serif;color:var(--white);background:var(--parchment)}
.abs{position:absolute}
.btn{position:absolute;display:flex;align-items:center;justify-content:center;background:var(--orange);color:var(--white);font-weight:700;font-size:14px;letter-spacing:.3px;text-decoration:none}

/* hero + header */
.hero{left:0;top:0;width:1200px;height:608px;background:linear-gradient(180deg,#c9903f 0%,#f3c766 30%,#f6d37a 42%,#e2a14c 60%,#c27a32 100%)}
.hero-glow{left:220px;top:260px;width:260px;height:160px;border-radius:50%;background:radial-gradient(circle,#fff4c4 0%,rgba(255,230,150,0) 70%)}
.site-header{left:0;top:0;width:1200px;height:84px;background:rgba(60,35,10,.45)}
.brand{left:74px;top:22px;font-size:30px;font-weight:800;letter-spacing:1px;color:var(--white)}
.main-nav{left:400px;top:32px;display:flex;gap:38px;font-size:13px;font-weight:700;color:var(--nav)}
.main-nav .active{color:#7a4a1c}
.hero-title{left:0;top:262px;width:1200px;text-align:center;color:var(--white);text-shadow:0 3px 6px rgba(0,0,0,.5)}
.hero-title .small{font-size:40px;font-weight:800;line-height:1}
.hero-title .big{font-size:82px;font-weight:800;line-height:1.05}
.dots{left:564px;top:562px;display:flex;gap:6px}
.dots span{width:14px;height:14px;border-radius:50%;background:var(--white)}
.dots span.on{background:#8a5221}

/* about */
.about{left:0;top:608px;width:1200px;height:307px;background:var(--brown);text-align:center}
.sec-title{font-size:26px;font-weight:700;letter-spacing:.5px}
.about .sec-title{position:absolute;left:0;top:50px;width:1200px}
.about p{position:absolute;left:80px;top:100px;width:1040px;font-size:15px;line-height:27px}

/* featured */
.featured{left:0;top:915px;width:1200px;height:513px;background:linear-gradient(135deg,var(--parchment-light),var(--parchment) 50%,#d99b4c)}
.featured .sec-title{position:absolute;left:76px;top:44px;color:var(--ink)}
.arrow{position:absolute;top:47px;width:24px;height:24px}
.card{position:absolute;top:99px;width:243px;height:367px;background:var(--card);border:2px solid var(--white)}
.card .photo{width:100%;height:178px}
.card h3{position:absolute;left:15px;top:200px;font-size:15px;font-weight:700;color:var(--yellow)}
.card p{position:absolute;left:15px;top:226px;width:210px;font-size:14px;line-height:23px}
.card .btn{left:15px;top:298px;width:160px;height:46px}

/* countries */
.countries{left:0;top:1428px;width:1200px;height:456px;background:var(--amber)}
.countries h2{position:absolute;left:130px;top:72px;width:420px;text-align:center;font-size:26px;line-height:34px;font-weight:700}
.countries p{position:absolute;left:80px;top:160px;width:520px;text-align:center;font-size:15px;line-height:27px}
.countries .btn{left:251px;top:331px;width:159px;height:42px}
.collage{left:600px;top:0;width:600px;height:456px;background:linear-gradient(90deg,#a46a2c,#7d4f23 40%,#9b6430)}

/* news */
.news{left:0;top:1884px;width:1200px;height:463px;background:linear-gradient(180deg,var(--parchment-light),var(--parchment))}
.news .sec-title{position:absolute;left:0;top:42px;width:1200px;text-align:center;color:var(--ink)}
.news-item{position:absolute;width:513px;height:142px;background:var(--brown)}
.news-item .thumb{position:absolute;left:15px;top:18px;width:156px;height:106px;border:2px solid var(--white)}
.news-item .date{position:absolute;left:190px;top:20px;font-size:15px;font-weight:700;color:var(--yellow)}
.news-item p{position:absolute;left:190px;top:44px;width:300px;font-size:14px;line-height:23px}
.news-item .more{position:absolute;left:190px;top:98px;font-size:12px;font-weight:700}

/* comments */
.comments{left:0;top:2347px;width:1200px;height:342px;background:var(--amber)}
.comments .sec-title{position:absolute;left:0;top:42px;width:1200px;text-align:center}
.quote{position:absolute;top:102px;width:330px}
.quote p{font-size:19px;line-height:29px;font-style:italic;font-weight:600}
.quote .name{margin-top:10px;font-size:14px;font-weight:700;color:var(--yellow)}
.quote .ago{font-size:13px;font-style:italic;font-weight:600}

/* footer */
.site-footer{left:0;top:2689px;width:1200px;height:159px;background:linear-gradient(135deg,var(--parchment-light),var(--parchment));color:var(--ink)}
.foot-nav{position:absolute;left:76px;top:45px;display:flex;gap:30px;font-size:12px;font-weight:600}
.copy{position:absolute;left:76px;top:82px;font-size:12px;line-height:22px}
.follow{position:absolute;left:931px;top:43px;font-size:14px;font-weight:700}
.social{position:absolute;left:926px;top:80px;display:flex;gap:16px}
.social span{width:22px;height:22px;border-radius:50%;background:#4a2e12}
</style>
</head>
<body>

<section class="abs hero">
  <div class="abs hero" role="img" aria-label="Desert dunes at sunset with a camel rider, a great pyramid and a golden winged ankh"></div>
  <div class="abs hero-glow"></div>
  <div class="abs hero-title"><div class="small">WELCOME TO</div><div class="big">TARN WISP</div></div>
  <div class="abs dots"><span class="on"></span><span></span><span></span><span></span></div>
</section>

<header class="abs site-header">
  <div class="abs brand">TARN WISP</div>
  <nav class="abs main-nav">
    <span class="active">HOME</span><span>ABOUT US</span><span>FEATURED ANCIENT ARTS/PLACES</span><span>LATEST NEWS</span><span>BLOG</span><span>CONTACT US</span>
  </nav>
</header>

<section class="abs about">
  <h2 class="sec-title">ABOUT TARN WISP</h2>
  <p>Aliquam molestie, mi et imperdiet euismod, dui purus auctor tellus, et interdum lacus lectus et ante. Sed accumsan sollicitudin sapien, sit amet adipiscing turpis gravida ac. In congue, neque ac lobortis volutpat, libero mauris varius mi, vitae suscipit ipsum ligula vitae risus. Duis aliquam nibh a dui iaculis viverra id a velit. Vivamus egestas risus in magna varius commodo. Sed semper viverra egestas.<br>Etiam pretium porttitor lectus, vel ornare neque porta volutpat.</p>
  <a class="btn" style="left:520px;top:228px;width:160px;height:44px">READ MORE</a>
</section>

<section class="abs featured">
  <h2 class="sec-title">FEATURED ANCIENT ARTS/PLACES</h2>
  <svg class="arrow" style="left:1073px" viewBox="0 0 24 24"><circle cx="12" cy="12" r="12" fill="#fff"/><path d="M14 7l-5 5 5 5" stroke="#2a1a0c" stroke-width="2.5" fill="none"/></svg>
  <svg class="arrow" style="left:1103px" viewBox="0 0 24 24"><circle cx="12" cy="12" r="12" fill="#2a1a0c"/><path d="M10 7l5 5-5 5" stroke="#fff" stroke-width="2.5" fill="none"/></svg>

  <article class="card" style="left:74px">
    <div class="photo" role="img" aria-label="Carved stone temple chariot" style="background:linear-gradient(180deg,#8a8a86,#6d5f4c)"></div>
    <h3>LOREM IPSUM</h3><p>Aliquam molestie, mi et imperdiet euismod, dui purus auctor tellus..</p><a class="btn">READ MORE</a>
  </article>
  <article class="card" style="left:344px">
    <div class="photo" role="img" aria-label="Ancient painted relief of a figure" style="background:linear-gradient(180deg,#c8a070,#a86a3e)"></div>
    <h3>LOREM IPSUM</h3><p>Aliquam molestie, mi et imperdiet euismod, dui purus auctor tellus..</p><a class="btn">READ MORE</a>
  </article>
  <article class="card" style="left:614px">
    <div class="photo" role="img" aria-label="Roman amphitheatre under a blue sky" style="background:linear-gradient(180deg,#5d8fd0,#b59a78 60%,#5b8a3a)"></div>
    <h3>LOREM IPSUM</h3><p>Aliquam molestie, mi et imperdiet euismod, dui purus auctor tellus..</p><a class="btn">READ MORE</a>
  </article>
  <article class="card" style="left:884px">
    <div class="photo" role="img" aria-label="Carved stone tablet with ancient figures" style="background:linear-gradient(180deg,#b58a68,#9a6e50)"></div>
    <h3>LOREM IPSUM</h3><p>Aliquam molestie, mi et imperdiet euismod, dui purus auctor tellus..</p><a class="btn">READ MORE</a>
  </article>
</section>

<section class="abs countries">
  <h2>COVERING A WIDE RANGE<br>OF COUNTRIES</h2>
  <p>Aliquam molestie, mi et imperdiet euismod, dui purus auctor tellus, et interdum lacus lectus et ante. Sed accumsan sollicitudin sapien, sit amet adipiscing turpis gravida ac. In congue, neque ac lobortis volutpat, libero mauris varius mi, vitae suscipit ipsum ligula vitae risus.<br>Duis aliquam nibh a dui iaculis viverra id a velit.</p>
  <a class="btn">READ MORE</a>
  <div class="abs collage" role="img" aria-label="Photo cards of Egypt, India, Syria, Greece and Rome pinned to a wooden board"></div>
</section>

<section class="abs news">
  <h2 class="sec-title">LATEST NEWS</h2>
  <article class="news-item" style="left:76px;top:111px">
    <div class="thumb" role="img" aria-label="Egyptian wall relief" style="background:linear-gradient(135deg,#c49a70,#8d6440)"></div>
    <div class="date">MAR 08, 2017</div><p>Aliquam molestie, mi et imperdiet euismod, dui purus auctor tellus..</p><div class="more">READ MORE</div>
  </article>
  <article class="news-item" style="left:614px;top:111px">
    <div class="thumb" role="img" aria-label="Carved temple columns" style="background:linear-gradient(135deg,#b0663a,#6a3a1e)"></div>
    <div class="date">MAR 08, 2017</div><p>Aliquam molestie, mi et imperdiet euismod, dui purus auctor tellus..</p><div class="more">READ MORE</div>
  </article>
  <article class="news-item" style="left:76px;top:269px">
    <div class="thumb" role="img" aria-label="Ornate red stone carving" style="background:linear-gradient(135deg,#c0705a,#7e3e30)"></div>
    <div class="date">MAR 08, 2017</div><p>Aliquam molestie, mi et imperdiet euismod, dui purus auctor tellus..</p><div class="more">READ MORE</div>
  </article>
  <article class="news-item" style="left:614px;top:269px">
    <div class="thumb" role="img" aria-label="Ruined stone pillars" style="background:linear-gradient(135deg,#a8b0b8,#7a6a58)"></div>
    <div class="date">MAR 08, 2017</div><p>Aliquam molestie, mi et imperdiet euismod, dui purus auctor tellus..</p><div class="more">READ MORE</div>
  </article>
</section>

<section class="abs comments">
  <h2 class="sec-title">RECENT COMMENTS</h2>
  <div class="quote" style="left:76px"><p>“ Aliquam molestie, mi et imperdiet euismod, dui purus auctor tellus, et interdum lacus lectus et accumsan sollicitudin sapien, sit amet adipiscing turpis gravida ac...”</p><div class="name">-Name Heading</div><div class="ago">1 min ago</div></div>
  <div class="quote" style="left:439px"><p>“ Aliquam molestie, mi et imperdiet euismod, dui purus auctor tellus, et interdum lacus lectus et accumsan sollicitudin sapien, sit amet adipiscing turpis gravida ac...”</p><div class="name">-Name Heading</div><div class="ago">1 min ago</div></div>
  <div class="quote" style="left:802px"><p>“ Aliquam molestie, mi et imperdiet euismod, dui purus auctor tellus, et interdum lacus lectus et accumsan sollicitudin sapien, sit amet adipiscing turpis gravida ac...”</p><div class="name">-Name Heading</div><div class="ago">1 min ago</div></div>
</section>

<footer class="abs site-footer">
  <nav class="foot-nav"><span>HOME</span><span>ABOUT US</span><span>FEATURED ANCIENT ARTS/PLACES</span><span>LATEST NEWS</span><span>BLOG</span><span>CONTACT US</span></nav>
  <div class="copy">Copyright © 2017 Company Name Right Reserved<br>Privacy Policy &nbsp;|&nbsp; Terms Of Conditions</div>
  <div class="follow">FOLLOW US</div>
  <div class="social"><span></span><span></span><span></span><span></span><span></span><span></span></div>
</footer>

</body>
</html>
```